Event branding Sales presentation PowerPoint template required

We are looking to freshen up & step up the professional quality of our powerpoint presentation template. I am looking for a professional designer with good creative background to design a new template for our presentations to new clients and for bespoke projects.
We have attached our current PPP as well as an elevator pitch which has most of the information we would like on the template

We have 3 main parts of our business which are:
- Event Branding
- Fan Engagements
- Set builds / Theming

Target Market(s)

Event organisers and sporting fedrations

Industry/Entity Type

Events

Requirements
Must have
• Ability for easy editing. Strong visual representation
Nice to have
• Information pages as well as look-book pages
Should not have
• Overcrowded graphics / arty graphics

```html
<!DOCTYPE html>
<html lang="en">
<head>
<meta charset="utf-8">
<title>Summit Events – Branding and Fan Engagement Template</title>
<link rel="stylesheet" href="https://fonts.googleapis.com/css2?family=Poppins:wght@400;500;600;700;800&display=swap">
<style>
  :root {
    --canvas: #3a3a3a;
    --gold: #c9a84a;
    --gold-deep: #3b3114;
    --ink: #0b0b0b;
    --white: #ffffff;
    --beige: #ece9df;
    --text-dark: #111111;
  }
  * { margin: 0; padding: 0; box-sizing: border-box; }
  html, body { width: 1200px; height: 2628px; overflow: hidden; background: var(--canvas); }
  body { font-family: "Poppins", Arial, sans-serif; position: relative; }

  .slide { position: absolute; left: 102px; width: 960px; height: 540px; overflow: hidden; }
  .slide > * { position: absolute; }
  .dot { color: var(--gold); }

  /* Slide 1: cover */
  .cover { top: 127px; background: linear-gradient(135deg, #141414 0%, #2a2a2a 55%, #1a1a1a 100%); }
  .cover .gold-rail { left: 0; top: 0; width: 48px; height: 540px; background: var(--gold); }
  .cover .brand { left: 80px; top: 72px; width: 160px; text-align: center; }
  .brand-ring { display: block; margin: 0 auto 12px; width: 70px; height: 70px; border: 1.5px solid var(--gold); border-radius: 50%; }
  .brand-name { color: var(--gold); font-size: 13px; letter-spacing: 3px; font-weight: 400; }
  .cover .photo-venue { left: 48px; top: 213px; width: 457px; height: 221px;
    background: linear-gradient(160deg, #b9c6cf 0%, #6b8a5a 40%, #2f5d8c 65%, #3e6e35 100%); }
  .cover .partner-band { left: 48px; top: 434px; width: 457px; height: 106px; background: #151515; }
  .cover .partner-badge { left: 76px; top: 456px; width: 114px; height: 55px; border: 1px solid #ffffff; background: #222; border-radius: 2px; }
  .cover .photo-wheel { left: 215px; top: 434px; width: 290px; height: 106px;
    background: radial-gradient(circle at 50% 60%, #6b5a22 0%, #2b2714 45%, #141410 100%); }
  .cover .photo-letters { left: 505px; top: 355px; width: 455px; height: 185px;
    background: linear-gradient(100deg, #8fd14a 0%, #8fd14a 28%, #f0705a 40%, #e95d88 55%, #46b39a 70%, #9fbf5a 85%, #5f7a3f 100%); }
  .cover .rule-v { left: 505px; top: 220px; width: 2px; height: 135px; background: var(--gold); }
  .cover .rule-h { left: 505px; top: 341px; width: 455px; height: 2px; background: var(--gold); opacity: .8; }
  .cover .title { left: 420px; top: 100px; color: var(--white); font-weight: 700; font-size: 60px; line-height: 70px; letter-spacing: -0.5px; }
  .cover .subtitle { left: 540px; top: 284px; }
  .subtitle-label { color: var(--gold); font-weight: 700; font-size: 15px; letter-spacing: 2px; }
  .subtitle-body { color: var(--white); font-size: 10px; margin-top: 2px; }

  /* Slide 2: contents */
  .contents { top: 738px; background: radial-gradient(ellipse at 75% 45%, #262626 0%, #121212 55%, #070707 100%); }
  .contents .black-rail { left: 0; top: 0; width: 48px; height: 493px; background: #000; }
  .contents .gold-block { left: 0; top: 493px; width: 48px; height: 47px; background: var(--gold); }
  .contents .photo-eye { left: 48px; top: 48px; width: 374px; height: 492px;
    background: linear-gradient(180deg, #3c1a18 0%, #9a3b12 35%, #c2561a 60%, #3a1f3c 85%, #c06ab8 100%); }
  .contents .title { left: 305px; top: 100px; color: var(--white); font-weight: 700; font-size: 60px; line-height: 70px; }
  .toc-item { width: 160px; }
  .toc-num { color: var(--gold-deep); font-weight: 800; font-size: 44px; line-height: 44px; }
  .toc-label { color: var(--white); font-weight: 700; font-size: 15px; line-height: 19px; letter-spacing: 2.5px; margin-top: 8px; }

  /* Slide 3: section divider */
  .divider { top: 1350px; background: linear-gradient(180deg, #2a1606 0%, #1b0f06 55%, #000 100%); }
  .divider .photo-silhouettes { left: 0; top: 0; width: 960px; height: 540px;
    background: radial-gradient(circle at 50% 35%, #6a5a08 0%, #4a3606 30%, #2a1606 55%, rgba(0,0,0,0) 80%),
                linear-gradient(180deg, rgba(0,0,0,0) 55%, #000 100%); }
  .divider .brand-mark { right: 48px; top: 45px; display: flex; align-items: center; gap: 10px; }
  .divider .brand-mark .brand-ring { width: 62px; height: 62px; margin: 0; }
  .divider .brand-mark .brand-name { font-size: 11px; }
  .divider .heading { left: 48px; top: 360px; color: var(--white); font-weight: 700; font-size: 36px; letter-spacing: 2px; line-height: 44px; }
  .divider .lede { left: 48px; top: 412px; color: var(--white); font-size: 15px; line-height: 21px; }
  .divider .rule { left: 48px; top: 490px; width: 712px; height: 1px; background: #2b2b2b; }
  .divider .section-num { left: 800px; top: 415px; color: var(--gold-deep); font-weight: 800; font-size: 84px; line-height: 90px; }

  /* Slide 4: welcome */
  .welcome { top: 1962px; background: var(--white); }
  .welcome .panel-beige { left: 352px; top: 0; width: 306px; height: 490px; background: var(--beige); }
  .welcome .gold-tick { left: 610px; top: 488px; width: 48px; height: 4px; background: var(--gold); }
  .welcome .photo-rig { left: 658px; top: 0; width: 302px; height: 540px;
    background: linear-gradient(180deg, #c9d2d4 0%, #4e6e5c 30%, #1f2a28 60%, #080808 100%); }
  .welcome .photo-rig-ring { left: 850px; top: 45px; width: 42px; height: 42px; border: 1.5px solid var(--gold); border-radius: 50%; }
  .welcome .title { left: 48px; top: 44px; color: var(--text-dark); font-weight: 700; font-size: 30px; }
  .welcome .intro { left: 48px; top: 170px; width: 260px; color: var(--gold); font-size: 15px; line-height: 21px; }
  .welcome .intro strong { font-weight: 700; }
  .welcome .body { left: 48px; top: 270px; width: 262px; color: var(--text-dark); font-size: 11.5px; line-height: 16px; }
  .note-bar { width: 42px; height: 5px; background: var(--gold); }
  .note-text { width: 210px; color: var(--text-dark); font-size: 9.5px; line-height: 13px; margin-top: 12px; }
  .welcome .note-one { left: 392px; top: 196px; }
  .welcome .note-two { left: 392px; top: 312px; }
  .welcome .tagline { left: 694px; top: 350px; width: 250px; color: var(--white); font-weight: 700; font-size: 27px; line-height: 37px; }
  .welcome .tagline .gold { color: var(--gold); }
</style>
</head>
<body>

<section class="slide cover">
  <div class="gold-rail"></div>
  <div class="brand"><span class="brand-ring"></span><div class="brand-name">SUMMIT EVENTS</div></div>
  <div class="photo-venue" role="img" aria-label="Aerial photo of a branded outdoor tennis venue"></div>
  <div class="partner-band"></div>
  <div class="partner-badge" role="img" aria-label="Partner badge"></div>
  <div class="photo-wheel" role="img" aria-label="Night photo of an illuminated observation wheel"></div>
  <div class="photo-letters" role="img" aria-label="Photo of giant colourful hashtag letters on a lawn"></div>
  <div class="rule-v"></div>
  <div class="rule-h"></div>
  <h1 class="title">Branding and<br>Fan Engagment<span class="dot">.</span></h1>
  <div class="subtitle">
    <div class="subtitle-label">INSERT SUBTITLE / PRESENTER NAME</div>
    <div class="subtitle-body">Lorem ipsum dolor sit amet, consectetur adipiscing elit.</div>
  </div>
</section>

<section class="slide contents">
  <div class="black-rail"></div>
  <div class="gold-block"></div>
  <div class="photo-eye" role="img" aria-label="Photo of an observation wheel at dusk with a suspended athlete sculpture"></div>
  <h2 class="title">Contents<span class="dot">.</span></h2>
  <div class="toc-item" style="left:457px;top:255px"><div class="toc-num">01.</div><div class="toc-label">ABOUT US</div></div>
  <div class="toc-item" style="left:594px;top:255px"><div class="toc-num">02.</div><div class="toc-label">UNIQUE<br>PERSPECTIVE</div></div>
  <div class="toc-item" style="left:761px;top:255px"><div class="toc-num">03.</div><div class="toc-label">TURNKEY<br>SOLUTIONS</div></div>
  <div class="toc-item" style="left:457px;top:381px"><div class="toc-num">04.</div><div class="toc-label">OUR<br>SERVICES</div></div>
  <div class="toc-item" style="left:594px;top:381px"><div class="toc-num">05.</div><div class="toc-label">PROJECT<br>EXAMPLES</div></div>
  <div class="toc-item" style="left:761px;top:381px"><div class="toc-num">06.</div><div class="toc-label">WHY SUMMIT<br>EVENTS?</div></div>
</section>

<section class="slide divider">
  <div class="photo-silhouettes" role="img" aria-label="Photo of visitors in silhouette before a glowing sphere installation"></div>
  <div class="brand-mark"><span class="brand-ring"></span><span class="brand-name">SUMMIT EVENTS</span></div>
  <h2 class="heading">ABOUT US<span class="dot">.</span></h2>
  <p class="lede">A brief overview<br>of Summit Events</p>
  <div class="rule"></div>
  <div class="section-num">01.</div>
</section>

<section class="slide welcome">
  <div class="panel-beige"></div>
  <div class="gold-tick"></div>
  <div class="photo-rig" role="img" aria-label="Photo of a performer rigged on a suspended wing inside an arena"></div>
  <div class="photo-rig-ring"></div>
  <h2 class="title">Welcome</h2>
  <p class="intro"><strong>Summit Events boasts<br>an international presence</strong><br>with established partners and relationships globally.</p>
  <p class="body">We punch well above our weight in the capability of our services. With a wealth of experience with venues &amp; events across the globe developing temporary &amp; permanent branding, themes, set builds, integrated rigging &amp; signage, your branding and fan engagement is in good hands with a partner who understands the changing demand for flexibility and quality.</p>
  <div class="note-one"><div class="note-bar"></div><p class="note-text">The Summit Events team have worked on iconic venues around the world including stadiums, Olympic parks, exhibition centres, dedicated event venues, museums and art galleries.</p></div>
  <div class="note-two"><div class="note-bar"></div><p class="note-text">The following will give you an idea about how Summit Events can work with Courtline League to take a step forward in your fan engagement and branding and we can also offer partnerships to sell media space at your venues.</p></div>
  <p class="tagline"><span class="gold">Pushing the boundaries,</span><br>delivering the highest quality.</p>
</section>

</body>
</html>
```